"Warm Coat RBK" Business Card/Logo Design

I'm looking for a very creative look for my new business called "Warm Coat RBK" on a business card design. Don't be distracted by my "business card details" below....if you have other ideas on how you see "Warm Coat RBK" go for it. If probably should somehow give a look that I paint furniture....maybe a paint drip or something simple or you can get more creative....sky's the limit and I really need your creative eye on how to per tray that "Warm Coat RBK" means taking something old and turning into new again with some paint.

Industry/Entity Type

Business

Contact Information for Business Card

I refurbish and up-cycle furniture that needs "a little TLC'....thus, my business name was born called "Warm Coat RBK" (Those are my initials). I mainly Giving tired furniture of every era a fresh new start again. I sometimes recreate furniture as well....I will make benches from old headboards of all sizes, etc. I'd love to see design that incorporate the crafty/creative side of me. If that means incorporating a paint brush, tools, paint cans, or furniture such as dressers, old vintage furniture, spindles, etc, etc. I don't know if something creative could be done with my initials (RBK). I really have a creative block of ideas and need your help bringing my "Warm Coat RBK" business to life.

P.S. Below is just one picture that I thought was neat and creative as they used a paintbrush but used spindles for the bristles and put their logo in the middle. Just an idea I thought was very unique and creative.

I'm very excited to see your design. Thank you for taking the time to create my logo/business card for me.

Rosa

Requirements
Must have
• Please include this information on the card:
• My Name: Rosa Kellerman
• Address: 48217 305th Ave NW, Pine Hollow, MN 55019
• E-Mail: warmcoatrbk@examplemail.net
• FB: http:/www.socialpage-sample.com/warmcoatrbk
• Cell: 555-014-2287

```html
<!DOCTYPE html>
<html lang="en">
<head>
<meta charset="utf-8">
<title>Warm Coat RBK – Business Card</title>
<link rel="stylesheet" href="https://fonts.googleapis.com/css2?family=Lato:wght@400;700&family=Dancing+Script:wght@700&display=swap">
<style>
  :root {
    --backdrop: #3a3240;
    --peach-light: #fde6d4;
    --peach-mid: #f6c39b;
    --orange-edge: #d9773f;
    --brown: #6a3718;
    --brown-dark: #2e180b;
    --black: #0b0706;
    --ink-red: #c8372a;
    --ring-brown: #6b3418;
    --text-light: #f6e3d2;
    --white: #ffffff;
  }
  html, body {
    margin: 0;
    padding: 0;
    width: 1200px;
    height: 800px;
    overflow: hidden;
    background: var(--backdrop);
  }
  .canvas {
    position: relative;
    width: 1200px;
    height: 800px;
    display: flex;
    align-items: center;
    justify-content: center;
  }
  .card {
    position: relative;
    width: 1050px;
    height: 600px;
    overflow: hidden;
    background: radial-gradient(ellipse 60% 70% at 55% 42%, var(--peach-light) 0%, var(--peach-mid) 55%, var(--orange-edge) 100%);
    font-family: "Lato", sans-serif;
  }
  .brand {
    position: absolute;
    left: 0;
    right: 0;
    top: 165px;
    display: flex;
    align-items: center;
    justify-content: center;
    gap: 18px;
  }
  .brand-dot {
    width: 34px;
    height: 34px;
    border-radius: 50%;
    background: var(--ring-brown);
  }
  .brand-name {
    font-weight: 700;
    font-size: 62px;
    color: var(--ink-red);
    letter-spacing: 1px;
  }
  .tagline {
    position: absolute;
    margin: 0;
    right: 40px;
    top: 322px;
    font-family: "Dancing Script", cursive;
    font-weight: 700;
    font-size: 33px;
    color: var(--black);
    white-space: nowrap;
  }
  .band {
    position: absolute;
    left: 0;
    top: 380px;
    width: 1050px;
    height: 220px;
  }
  .holder-name {
    position: absolute;
    left: 34px;
    top: 385px;
    font-size: 32px;
    color: var(--white);
  }
  .address {
    position: absolute;
    left: 34px;
    top: 450px;
    font-size: 22px;
    line-height: 1.35;
    color: var(--text-light);
  }
  .social {
    position: absolute;
    right: 40px;
    top: 391px;
    display: flex;
    align-items: center;
    gap: 10px;
    font-size: 24px;
    color: var(--white);
  }
  .social-square {
    width: 20px;
    height: 20px;
    background: var(--orange-edge);
  }
  .contact {
    position: absolute;
    right: 40px;
    top: 470px;
    text-align: right;
    font-size: 24px;
    line-height: 1.45;
    color: var(--text-light);
  }
</style>
</head>
<body>
<main class="canvas">
  <section class="card" aria-label="Warm Coat RBK business card">
    <div class="brand">
      <span class="brand-dot" aria-hidden="true"></span>
      <span class="brand-name">Warm Coat RBK</span>
    </div>
    <p class="tagline">Giving tired furniture of every era a fresh new start again</p>

    <svg class="band" viewBox="0 0 1050 220" aria-hidden="true">
      <rect x="0" y="0" width="1050" height="220" fill="var(--brown)"/>
      <polygon points="690,0 1050,0 1050,52 690,52" fill="var(--brown-dark)"/>
      <polygon points="0,0 760,0 700,52 0,52" fill="var(--black)"/>
    </svg>

    <div class="holder-name">Rosa Kellerman</div>
    <div class="address">48217 305th Ave NW, Pine Hollow<br>MN 55019</div>

    <div class="social">
      <span class="social-square" aria-hidden="true"></span>
      <span>warmcoatrbk</span>
    </div>
    <div class="contact">
      Email: warmcoatrbk@examplemail.net<br>
      Phone: 555-014-2287
    </div>
  </section>
</main>
</body>
</html>
```